Reach Far Goals Training Web Design and Launch!

A recently new business in Personal Coaching (Fitness) looking to have a professional website built along with using Coinwell system for payments. Ability to set up memberships would be great. Current site is www.rfgtrain.fit . I used that site to quickly put something together so that I could get started. Also looking to do something similar to www.morlandgym.com with a shop as well as challenges and leaderboards that members and non members alike can participate in. Would like to have a "meet the coaches" page option along with what I currently have on the site.

Target Market(s)

Men and Women 24-60 years old. Weight loss clients

Industry/Entity Type

Fitness

Coding

Coded - Design and coding required

Number of Pages Required

5+ page

Font styles to use
Sans Serif

Colors
33a6d7
f78f20
0255a3
0592cd

Requirements
Must have
• Coinwell or Payment integration. Photo gallery. Reviews page. Calender link for events. Donation location for Step4AllKin
Nice to have
• Would like to have a page dedicated to challenges/leaderboards. A way for members and non members to input their results of a posted challenge. Like to have similar pages that my current site www.rfgtrain.fit has. Ways to sign up for a membership. Meet the coaches and athletes. Gallery designed to call out award winning performances (podium or series wins), Meet the coaches and athletes.

```html
<!DOCTYPE html>
<html lang="en">
<head>
<meta charset="utf-8">
<title>Reach Far Goals Training</title>
<link href="https://fonts.googleapis.com/css2?family=Montserrat:wght@500;600;700;800&family=Open+Sans:wght@400;600&display=swap" rel="stylesheet">
<style>
:root{
  --orange:#f78f20;
  --blue-deep:#0255a3;
  --blue-mid:#0592cd;
  --blue-light:#33a6d7;
  --card-blue:#1e90e6;
  --ink:#222;
  --text:#666;
  --dark:#242424;
  --footer:#1f2326;
  --white:#fff;
}
*{box-sizing:border-box;margin:0;padding:0}
html,body{width:1200px;height:5270px;overflow:hidden}
body{font-family:"Open Sans",Arial,sans-serif;color:var(--text);background:#fff;position:relative}
.section{position:relative;width:1200px;overflow:hidden}
.abs{position:absolute}
.heading{font-family:"Montserrat",Arial,sans-serif;font-weight:700;color:var(--ink);font-size:33px;text-align:center;width:100%;letter-spacing:.5px}
.sub{font-size:12.5px;text-align:center;width:100%;color:#555}
.btn{display:flex;align-items:center;justify-content:center;background:var(--orange);color:#fff;font-family:"Montserrat",sans-serif;font-weight:700;font-size:10px;text-transform:uppercase;letter-spacing:.5px}
.photo{position:absolute}

/* header */
.topbar{height:65px;background:#262626}
.brand{left:92px;top:6px;display:flex;flex-direction:column;align-items:center;width:60px}
.brand-dot{width:34px;height:34px;border-radius:50%;border:3px solid #fff}
.brand-name{color:#fff;font-family:"Montserrat",sans-serif;font-weight:700;font-size:6px;text-align:center;line-height:1.15;margin-top:3px;text-transform:uppercase}
.login{left:977px;top:16px;width:129px;height:33px;font-size:10px;font-weight:600}
.navbar{height:47px;border-bottom:1px solid #e5e5e5;background:#fff}
.nav-link{top:18px;font-family:"Montserrat",sans-serif;font-size:10.5px;font-weight:500;color:#444;text-transform:uppercase}
.nav-link.active{color:var(--blue-light)}
.social{top:13px;display:flex;gap:6px}
.social span{width:20px;height:20px;border-radius:50%;background:#222;display:block}

/* hero */
.hero{height:487px}
.hero-title{left:274px;top:174px;width:652px;height:133px;background:rgba(20,20,20,.82)}
.hero-title h1{font-family:"Montserrat",sans-serif;font-weight:700;color:#fff;font-size:49px;white-space:nowrap;text-align:center;margin-top:22px;letter-spacing:0}
.hero-title p{font-family:"Montserrat",sans-serif;font-weight:700;color:var(--orange);font-size:18px;text-align:center;margin-top:16px;letter-spacing:1.5px}

/* who we are */
.who{height:1121px}
.who-bubble{left:310px;top:990px;width:580px;height:580px;border-radius:50%;background:#eef7fc}
.feature{width:440px;text-align:center}
.feature h3{font-family:"Montserrat",sans-serif;font-weight:500;color:#222;font-size:20px}
.feature .rule{width:38px;height:2px;background:var(--orange);margin:9px auto 14px}
.feature p{font-size:11.5px;line-height:21px;color:#666}

/* events */
.events{height:559px}
.event{width:327px}
.event .pic{position:relative;height:225px}
.date{position:absolute;right:0;bottom:0;width:70px;height:70px;background:linear-gradient(135deg,transparent 50%,var(--orange) 50%);color:#fff;text-align:right;padding:30px 6px 0 0;font-family:"Montserrat",sans-serif}
.date b{font-size:13px;display:block;line-height:14px}
.date small{font-size:6px;letter-spacing:1px;display:block}
.event h4{font-family:"Montserrat",sans-serif;font-weight:500;color:#222;font-size:20px;margin-top:14px}
.event p{font-size:10px;line-height:16px;color:#777;margin-top:8px;width:290px}
.event .btn{width:115px;height:33px;margin-top:25px}
.arrow{top:222px;width:30px;height:30px;border-radius:50%;border:1px solid #ddd;background:#fff;display:flex;align-items:center;justify-content:center}

/* cause */
.cause{height:405px;background:linear-gradient(120deg,#0a5fb2,var(--blue-deep))}
.cause h2{font-family:"Montserrat",sans-serif;font-weight:700;color:#fff;font-size:34px;left:601px;top:90px}
.cause p{left:601px;top:143px;width:510px;color:#e6f0fa;font-size:11.5px;line-height:21px}
.donate{left:601px;top:217px;width:146px;height:35px;border-radius:18px;font-size:11px}
.pay-note{left:621px;top:259px;color:#fff;text-align:center;width:105px}
.pay-note small{font-size:5.5px;display:block}
.pay-note b{font-family:"Montserrat",sans-serif;font-size:13px;font-weight:700}
.chips{left:604px;top:290px;display:flex;gap:3px}
.chips span{width:20px;height:12px;background:#fff;border-radius:2px;display:block}

/* coaches */
.coaches{height:509px}
.coach{top:161px;width:180px;height:282px}
.coach .pic{position:absolute;inset:0 0 20px 0;border-radius:90px 90px 0 0}
.coach .label{position:absolute;left:15px;right:15px;bottom:0;height:72px;background:var(--blue-mid);border-radius:75px 75px 0 0;text-align:center;color:#fff;padding-top:20px}
.coach .label b{font-family:"Montserrat",sans-serif;font-weight:600;font-size:14px;display:block}
.coach .label small{font-size:9px}

/* reviews */
.reviews{height:588px;background:linear-gradient(180deg,#0a4fa0,#0255a3)}
.reviews .heading{color:#fff}
.reviews .sub{color:#d7e7f7}
.review{top:208px;width:321px;height:305px;background:var(--card-blue);text-align:center;color:#fff}
.avatar{position:absolute;top:-43px;left:118px;width:84px;height:84px;border-radius:50%;border:3px solid #fff}
.review .rec{font-family:"Montserrat",sans-serif;font-weight:500;font-size:13px;margin-top:60px}
.stars{color:var(--orange);font-size:11px;letter-spacing:1px}
.review q{display:block;font-size:11.5px;line-height:20px;width:240px;margin:12px auto 0;color:#e4f1fd;quotes:none}
.review .icon{width:22px;height:22px;border-radius:50%;background:#fff;margin:10px auto 0}
.review .who-name{font-family:"Montserrat",sans-serif;font-weight:600;font-size:15px;margin-top:6px}
.review .date-line{font-size:10px;color:#d5e8fb}
.review .btn{width:115px;height:33px;margin:12px auto 0}

/* challenges */
.challenges{height:542px;background:#1e1e1e}
.challenges .heading{color:#fff}
.circle-shot{width:296px;height:296px;border-radius:50%;border:3px solid #fff}
.ch-text{width:215px}
.ch-text h3{font-family:"Montserrat",sans-serif;font-weight:500;font-size:24px;color:#fff}
.ch-text h3 span{color:var(--orange)}
.ch-text p{color:#cfcfcf;font-size:12px;line-height:21px;margin-top:10px}
.pip{width:6px;height:6px;border-radius:50%;background:var(--blue-light)}

/* instagram */
.instagram{height:542px}
.grid{left:92px;top:117px;width:1014px;height:364px;display:grid;grid-template-columns:repeat(4,1fr);grid-template-rows:repeat(2,1fr)}
.grid div{position:relative}

/* footer */
.footer{height:405px;background:var(--footer);color:#c7c7c7}
.col-title{top:45px;font-family:"Montserrat",sans-serif;font-weight:500;font-size:17px;color:#fff}
.links{top:82px;font-size:10px;line-height:26px;color:#b8b8b8;list-style:none}
.contact-line{font-size:10px;color:#b8b8b8;display:flex;align-items:center;gap:6px}
.field{left:836px;width:270px;height:30px;background:#fff;font-size:9px;color:#777;padding:9px 12px}
.subscribe{left:836px;top:140px;width:270px;height:31px;font-size:11px;font-weight:600;text-transform:none}
.foot-brand{left:540px;top:228px;width:120px;display:flex;flex-direction:column;align-items:center}
.foot-brand .brand-dot{width:58px;height:58px;border-width:5px}
.foot-brand .brand-name{font-size:8px}
.copy{top:317px;width:100%;text-align:center;font-size:9.5px;color:#aaa}
.copy b{color:#fff;font-weight:600}
.cards{top:337px;left:530px;display:flex;gap:5px}
.cards span{width:30px;height:18px;background:#e9e9e9;border-radius:2px;display:block}
.partner{left:990px;top:334px;display:flex;align-items:center;gap:6px;font-size:9px;color:#ccc}
.partner span{width:58px;height:28px;background:#fff;display:block}
</style>
</head>
<body>

<!-- top bar -->
<header class="section topbar">
  <div class="abs brand"><span class="brand-dot"></span><span class="brand-name">Reach Far Goals Training</span></div>
  <div class="abs btn login">
    <svg width="11" height="11" viewBox="0 0 12 12" style="margin-right:6px"><circle cx="6" cy="4" r="2.5" fill="none" stroke="#fff" stroke-width="1.2"/><path d="M1.5 11.5c0-2.5 2-4 4.5-4s4.5 1.5 4.5 4" fill="none" stroke="#fff" stroke-width="1.2"/></svg>MEMBER LOGIN
  </div>
</header>

<nav class="section navbar">
  <span class="abs nav-link active" style="left:92px">Home</span>
  <span class="abs nav-link" style="left:174px">Gallery</span>
  <span class="abs nav-link" style="left:272px">Reviews</span>
  <span class="abs nav-link" style="left:370px">Blog</span>
  <span class="abs nav-link" style="left:450px">Contact Us</span>
  <span class="abs nav-link" style="left:569px">Athlete Page</span>
  <div class="abs social" style="left:1032px"><span></span><span></span><span></span></div>
</nav>

<!-- hero -->
<section class="section hero">
  <div class="photo" role="img" aria-label="Female coach running a trail race" style="left:0;top:0;width:300px;height:487px;background:linear-gradient(160deg,#8d8a80,#4b4a46)"></div>
  <div class="photo" role="img" aria-label="Male coach lifting in a bright gym" style="left:300px;top:0;width:300px;height:487px;background:linear-gradient(180deg,#e0b52a,#6f6a60)"></div>
  <div class="photo" role="img" aria-label="Female athlete jogging" style="left:600px;top:0;width:300px;height:487px;background:linear-gradient(180deg,#141414,#3a3632)"></div>
  <div class="photo" role="img" aria-label="Male coach in a grey training shirt" style="left:900px;top:0;width:300px;height:487px;background:linear-gradient(180deg,#dcdcd8,#6e6e6a)"></div>
  <div class="abs hero-title">
    <h1>COACHES WHO CARE</h1>
    <p>LET'S WORK OUT TOGETHER!</p>
  </div>
</section>

<!-- who we are -->
<section class="section who">
  <div class="abs who-bubble"></div>
  <h2 class="abs heading" style="top:56px">WHO WE ARE</h2>

  <div class="photo" role="img" aria-label="Coach helping a client with a weight plate exercise" style="left:92px;top:131px;width:507px;height:320px;background:linear-gradient(120deg,#d9d4cc,#8b857c)"></div>
  <div class="abs feature" style="left:649px;top:221px">
    <h3>Coaches Who Care</h3><div class="rule"></div>
    <p>Our coaches take your fitness goals seriously. We understand that losing weight and gaining muscle can be challenging, and our goal is to help you overcome hurdles and reach your goals. We analyze your body type, BMI, and metabolism, to create your individualized fitness plan.</p>
  </div>

  <div class="photo" role="img" aria-label="Coach reviewing a plan on a clipboard with a client" style="left:599px;top:452px;width:507px;height:319px;background:linear-gradient(120deg,#e8e8e6,#7b7d80)"></div>
  <div class="abs feature" style="left:126px;top:542px">
    <h3>Knowledgeable Training Expertise</h3><div class="rule"></div>
    <p>With years of success and experience, we are capable of analyzing your body and creating a fitness plan that will help you reach your goals. Most plans include healthy eating and exercise, to ensure the best results for our clients. Our coaches will work with you to keep you on track and motivated to reach your goals.</p>
  </div>

  <div class="photo" role="img" aria-label="Athlete bending for a heavy carry at an obstacle race" style="left:92px;top:771px;width:507px;height:320px;background:linear-gradient(120deg,#6d6d6d,#2c2c2c)"></div>
  <div class="abs feature" style="left:649px;top:838px">
    <h3>Your Success is Our Goal</h3><div class="rule"></div>
    <p>We understand that adapting new fitness habits is difficult and often times fails. Our goal is to change your view on fitness, so that it becomes apart of who you are and your lifestyle. We strongly believe that if you practice healthy habits, you will be able to obtain a healthy lifestyle. As a team we will have you feeling your best and maybe even finding yourself competing in a competition or in obstacle course racing.</p>
  </div>
</section>

<!-- races and events -->
<section class="section events">
  <h2 class="abs heading" style="top:36px">RACES AND EVENTS</h2>
  <p class="abs sub" style="top:85px;font-size:11.5px">Keep an eye out and you may see a RFG Coach or Athlete at these events!</p>

  <div class="abs arrow" style="left:30px"><svg width="10" height="10" viewBox="0 0 10 10"><path d="M6.5 1.5 3 5l3.5 3.5" fill="none" stroke="#333" stroke-width="1.4"/></svg></div>
  <div class="abs arrow" style="left:1137px"><svg width="10" height="10" viewBox="0 0 10 10"><path d="M3.5 1.5 7 5 3.5 8.5" fill="none" stroke="#333" stroke-width="1.4"/></svg></div>

  <article class="abs event" style="left:92px;top:126px">
    <div class="pic" role="img" aria-label="Team posing at a stadium race finish" style="background:linear-gradient(180deg,#8a8f98,#3b3e45)"><div class="date"><b>4th</b><small>APRIL</small></div></div>
    <h4>Titan Stadion Harbor Field</h4>
    <p>If you use this site regularly and would like to help keep the site on the Interne...</p>
    <div class="btn">Read More</div>
  </article>
  <article class="abs event" style="left:435px;top:126px">
    <div class="pic" role="img" aria-label="Runner on a stadium field course" style="background:linear-gradient(180deg,#9fa39c,#4f7a3f)"><div class="date"><b>7th</b><small>APRIL</small></div></div>
    <h4>Titan Race Pine Ridge Beast</h4>
    <p>If you use this site regularly and would like to help keep the site on the Interne...</p>
    <div class="btn">Read More</div>
  </article>
  <article class="abs event" style="left:779px;top:126px">
    <div class="pic" role="img" aria-label="Group of racers with medals" style="background:linear-gradient(180deg,#8d9aa6,#3f4a3c)"><div class="date"><b>20th</b><small>JUNE</small></div></div>
    <h4>Titan Stadion Bay Park</h4>
    <p>If you use this site regularly and would like to help keep the site on the Interne...</p>
    <div class="btn">Read More</div>
  </article>
</section>

<!-- help our cause -->
<section class="section cause">
  <div class="photo" role="img" aria-label="Athlete pushing a racing wheelchair on a city street" style="left:0;top:0;width:605px;height:405px;clip-path:polygon(0 0,605px 0,460px 405px,0 405px);background:linear-gradient(120deg,#9a9da0,#545a5f)"></div>
  <svg class="abs" style="left:0;top:0" width="1200" height="405" viewBox="0 0 1200 405"><path d="M605 0 460 405 475 405 620 0Z" fill="#0592cd"/></svg>
  <h2 class="abs">HELP OUR CAUSE</h2>
  <p class="abs">In 2020 we are looking to support Step4AllKin an organization focused on helping people move and giving all athletes the opportunity to cross the finish line! Your generous donation will fund our mission.</p>
  <div class="abs btn donate">Donate Now</div>
  <div class="abs pay-note"><small>Secured Payments by</small><b>Coinwell</b></div>
  <div class="abs chips"><span></span><span></span><span></span><span></span></div>
</section>

<!-- meet the coaches -->
<section class="section coaches">
  <h2 class="abs heading" style="top:56px">MEET THE COACHES</h2>
  <p class="abs sub" style="top:100px;font-size:11.5px">If you use this site regularly and would like to help keep the site on the Internet, please consider donating</p>

  <div class="abs coach" style="left:129px">
    <div class="pic" role="img" aria-label="Portrait of coach on yellow" style="background:linear-gradient(180deg,#f6c62b,#e6a91a)"></div>
    <div class="label"><b>Mr. Jhon Doe</b><small>Fitness Trainer</small></div>
  </div>
  <div class="abs coach" style="left:382px">
    <div class="pic" role="img" aria-label="Portrait of coach on dark grey" style="background:linear-gradient(180deg,#4d4d4d,#242424)"></div>
    <div class="label"><b>Mr. Jhon Lux</b><small>Fitness Trainer</small></div>
  </div>
  <div class="abs coach" style="left:636px">
    <div class="pic" role="img" aria-label="Portrait of coach on yellow" style="background:linear-gradient(180deg,#f6c62b,#e6a91a)"></div>
    <div class="label"><b>Miss. Alexa Paul</b><small>Fitness Trainer</small></div>
  </div>
  <div class="abs coach" style="left:889px">
    <div class="pic" role="img" aria-label="Portrait of coach on light background" style="background:linear-gradient(180deg,#f1f3f5,#d5dbe1)"></div>
    <div class="label"><b>Mr. Paul Adms</b><small>Fitness Trainer</small></div>
  </div>
</section>

<!-- reviews -->
<section class="section reviews">
  <h2 class="abs heading" style="top:66px">REVIEWS</h2>
  <p class="abs sub" style="top:117px;font-size:11.5px">Reach Far Goals Training 100% recommend Based on the opinion of 4 people</p>

  <article class="abs review" style="left:92px">
    <div class="avatar" role="img" aria-label="Reviewer photo" style="background:linear-gradient(180deg,#c9c3bb,#7c746b)"></div>
    <p class="rec">Recommends</p><div class="stars">★★★★★</div>
    <q>"I would recommend Marco to anybody looking to take their li..."</q>
    <div class="icon"></div>
    <p class="who-name">Renata Calloway</p><p class="date-line">2/29/2020</p>
    <div class="btn">Read More</div>
  </article>
  <article class="abs review" style="left:439px">
    <div class="avatar" role="img" aria-label="Reviewer photo" style="background:linear-gradient(180deg,#b9b9b9,#444)"></div>
    <p class="rec">Recommends</p><div class="stars">★★★★★</div>
    <q>My experience with Reach Far Goals Coaching and Marco ha..."</q>
    <div class="icon"></div>
    <p class="who-name">Dominic R Ashby</p><p class="date-line">2/29/2020</p>
    <div class="btn">Read More</div>
  </article>
  <article class="abs review" style="left:786px">
    <div class="avatar" role="img" aria-label="Reviewer photo" style="background:linear-gradient(180deg,#d6c2b2,#7d5a48)"></div>
    <p class="rec">Recommends</p><div class="stars">★★★★★</div>
    <q>Marco is amazing! He really knows how to push you and he..."</q>
    <div class="icon"></div>
    <p class="who-name">Lena Marsh</p><p class="date-line">2/29/2020</p>
    <div class="btn">Read More</div>
  </article>
</section>

<!-- challenges -->
<section class="section challenges">
  <h2 class="abs heading" style="top:56px">CHALLENGES</h2>
  <svg class="abs" style="left:0;top:0" width="1200" height="542" viewBox="0 0 1200 542">
    <path d="M240 285 Q600 70 960 285" fill="none" stroke="#6a6a6a" stroke-dasharray="3 4"/>
  </svg>
  <div class="abs pip" style="left:237px;top:278px"></div>
  <div class="abs pip" style="left:957px;top:278px"></div>
  <div class="abs circle-shot" role="img" aria-label="Torso before the fitness program, black and white" style="left:322px;top:190px;background:radial-gradient(circle at 50% 45%,#d8d8d8,#7a7a7a)"></div>
  <div class="abs circle-shot" role="img" aria-label="Torso after the fitness program" style="left:582px;top:190px;background:radial-gradient(circle at 50% 45%,#e9c7ae,#8a6550)"></div>
  <div class="abs ch-text" style="left:92px;top:289px">
    <h3><span>Before</span> Fitness</h3>
    <p>Sed ut perspiciatis unde omnis iste natus error sit voluptatem accusantium doloremque laudantium, totam rem aperiam.</p>
  </div>
  <div class="abs ch-text" style="left:892px;top:289px">
    <h3><span>After</span> Fitness</h3>
    <p>Sed ut perspiciatis unde omnis iste natus error sit voluptatem accusantium doloremque laudantium, totam rem aperiam.</p>
  </div>
</section>

<!-- instagram -->
<section class="section instagram">
  <h2 class="abs heading" style="top:58px">INSTAGRAM</h2>
  <div class="abs grid">
    <div role="img" aria-label="Runner on a stadium field" style="background:linear-gradient(180deg,#9ea4a0,#4b7a3e)"></div>
    <div role="img" aria-label="Athletes at a ballpark obstacle" style="background:linear-gradient(180deg,#6d7890,#3b3f4a)"></div>
    <div role="img" aria-label="Group training outdoors" style="background:linear-gradient(180deg,#b8b5ae,#5c5a54)"></div>
    <div role="img" aria-label="Coach at an event" style="background:linear-gradient(180deg,#5a5a5a,#222)"></div>
    <div role="img" aria-label="Runners on a street course" style="background:linear-gradient(180deg,#c8c8c6,#6a6a6a)"></div>
    <div role="img" aria-label="Athlete flexing, orange overlay" style="background:linear-gradient(180deg,#f7a13a,#f08a1c)">
      <svg style="position:absolute;left:113px;top:77px" width="28" height="28" viewBox="0 0 28 28" fill="none" stroke="#fff" stroke-width="1.6"><path d="M3 10V3h7M3 3l8 8M25 10V3h-7M25 3l-8 8M3 18v7h7M3 25l8-8M25 18v7h-7M25 25l-8-8"/></svg>
    </div>
    <div role="img" aria-label="Coach portrait on dark backdrop" style="background:linear-gradient(180deg,#4a4a4a,#1a1a1a)"></div>
    <div role="img" aria-label="Athlete competing outdoors" style="background:linear-gradient(180deg,#7d8a78,#3d4636)"></div>
  </div>
  <div class="abs" style="left:576px;top:488px;width:6px;height:6px;border-radius:50%;background:#999"></div>
</section>

<!-- footer -->
<footer class="section footer">
  <h4 class="abs col-title" style="left:92px">Quick Links</h4>
  <ul class="abs links" style="left:92px"><li>Home</li><li>Shop</li><li>Contact Us</li><li>Blog</li><li>Athlete</li></ul>

  <h4 class="abs col-title" style="left:321px">Shop</h4>
  <ul class="abs links" style="left:321px"><li>Virtual Coaching</li><li>Sports Specific Coaching</li><li>Full Service Coaching</li><li>Nutritional Guidance</li><li>Military PT</li></ul>

  <h4 class="abs col-title" style="left:580px">Contact Us</h4>
  <div class="abs contact-line" style="left:580px;top:84px">
    <svg width="9" height="11" viewBox="0 0 9 11"><path d="M4.5 0.5a3.5 3.5 0 0 1 3.5 3.5c0 2.6-3.5 6.5-3.5 6.5S1 6.6 1 4a3.5 3.5 0 0 1 3.5-3.5Z" fill="var(--orange)"/></svg>+1 555-014-2290
  </div>
  <div class="abs contact-line" style="left:580px;top:114px">
    <svg width="11" height="8" viewBox="0 0 11 8"><rect width="11" height="8" rx="1" fill="var(--orange)"/><path d="M0.5 0.5 5.5 4.5 10.5 0.5" fill="none" stroke="#1f2326"/></svg>coachmarco@rfgtrain.fit
  </div>
  <p class="abs" style="left:580px;top:148px;font-size:11.5px;color:#fff">Follow Us on</p>
  <div class="abs social" style="left:580px;top:167px"><span style="background:#fff"></span><span style="background:#fff"></span><span style="background:#fff"></span></div>

  <h4 class="abs col-title" style="left:836px">Newsletter</h4>
  <div class="abs field" style="top:70px">Enter Your Name</div>
  <div class="abs field" style="top:105px">Enter Your Email</div>
  <div class="abs btn subscribe">Subscribe</div>

  <div class="abs foot-brand"><span class="brand-dot"></span><span class="brand-name">Reach Far Goals Training</span></div>
  <p class="abs copy">COPYRIGHT © 2020 <b>REACH FAR GOALS TRAINING</b>. ALL RIGHTS RESERVED.</p>
  <div class="abs cards"><span></span><span></span><span></span><span></span></div>
  <div class="abs partner">Our Partner <span></span></div>
</footer>

</body>
</html>
```